Business card, Sationery for Surgery center
KTLM Coralview Outpatient Surgery Center
Business card, Sationery for Surgery center - Health
Creative Brief
Simple
Marisol Quenby-Harcourt
Director
42 Heron Gate Lane Paget RH19 Bermuda Mailing Adress: PO Box KM37, Devonshire LQTZ, Bermuda
info@ktlm-example.bm
www.ktlm-example.bm

```html
<!DOCTYPE html>
<html lang="en">
<head>
<meta charset="utf-8">
<title>KTLM Stationery Concepts</title>
<link href="https://fonts.googleapis.com/css2?family=Open+Sans:wght@400;600;700&family=Great+Vibes&display=swap" rel="stylesheet">
<style>
:root{
  --bg:#3b3b3b;
  --blue:#1a4fc4;
  --green:#7dc21e;
  --paper:#ffffff;
  --ink:#2e2e2e;
  --muted:#666;
  --pale:#dfe6ff;
}
*{box-sizing:border-box;margin:0;padding:0}
html,body{width:1200px;height:254px;overflow:hidden;background:var(--bg);font-family:"Open Sans",sans-serif;color:var(--ink)}
.canvas{position:relative;width:1200px;height:254px}
.piece{position:absolute;background:var(--paper);overflow:hidden}
.label{position:absolute;font-size:2.6px;color:#d0d0d0;text-align:center}
.mark{font-weight:700;color:var(--blue);letter-spacing:.2px;line-height:1;display:inline-flex;align-items:center;gap:1px}
.mark .dot{display:inline-block;border-radius:50%;background:var(--green)}
.mark.light{color:#fff}
.tag{font-size:1.7px;font-weight:600;color:var(--blue);letter-spacing:.1px;line-height:2.2px}
.tag.light{color:var(--pale)}
.tiny{font-size:2.3px;line-height:3px;color:var(--muted)}
.tiny b{color:var(--ink);font-weight:700}
.tiny.light{color:var(--pale)}
.tiny.light b{color:#fff}
.title-block{position:absolute;left:34px;top:30px;width:58px;text-align:center;color:#eee}
.title-block .mark{color:#fff;font-size:9px}
.title-block p{font-size:3.6px;margin-top:2px;color:#e0e0e0}
.script{font-family:"Great Vibes",cursive;color:var(--blue)}
.slide-h{font-size:4px;font-weight:700;color:var(--blue);line-height:4.6px}
.slide-s{font-size:2.2px;color:var(--green)}
.rule{height:.4px;background:var(--green);margin:1px 0 3px}
.photo{background:linear-gradient(#6a6a6a,#4a4a4a);font-size:2.2px;color:#ddd;display:flex;align-items:center;justify-content:center}
.disc{position:absolute;border-radius:50%;display:flex;flex-direction:column;align-items:center;justify-content:center}
.disc .top{position:absolute;top:7px;display:flex;flex-direction:column;align-items:center}
.disc .url{position:absolute;bottom:7px;font-size:2.2px}
.hole{width:30%;height:30%;border-radius:50%;background:#fff;border:1.5px solid #222}
.field{display:flex;gap:1px;align-items:center}
.field i{flex:1;height:2.4px;background:#eee;display:block}
.foot{position:absolute;bottom:3px;left:0;right:0;text-align:center}
</style>
</head>
<body>
<div class="canvas">

  <div class="title-block">
    <div class="mark"><span class="dot" style="width:4px;height:4px"></span>KTLM</div>
    <p>Stationary Concepts</p>
  </div>

  <!-- business cards -->
  <div class="piece" style="left:7px;top:57px;width:47px;height:27px">
    <div style="position:absolute;right:0;top:0;width:17px;height:27px;background:var(--green)"></div>
    <div style="padding:2px 3px;width:31px">
      <div class="mark" style="font-size:5.5px">KTLM</div>
      <div class="tiny" style="font-size:1.9px;line-height:2.5px;margin-top:1.5px"><b style="color:var(--blue)">Marisol Quenby-Harcourt</b><br>Director<br>42 Heron Gate Lane<br>Paget RH19 Bermuda<br>T 441-555-0148<br>info@ktlm-example.bm</div>
    </div>
  </div>
  <div class="label" style="left:7px;top:85px;width:47px">Front Card</div>
  <div class="piece" style="left:59px;top:57px;width:47px;height:27px;display:flex;flex-direction:column;align-items:center;justify-content:center">
    <div class="mark" style="font-size:7px"><span class="dot" style="width:2.5px;height:2.5px"></span>KTLM</div>
    <div class="tag" style="margin-top:.6px">CORALVIEW OUTPATIENT SURGERY CENTER</div>
    <div class="tiny" style="margin-top:3px">www.ktlm-example.bm</div>
  </div>
  <div class="label" style="left:59px;top:85px;width:47px">Back Card</div>

  <!-- letterheads -->
  <div class="piece" style="left:109px;top:16px;width:78px;height:101px;padding:4px 5px">
    <div class="mark" style="font-size:5px">KTLM</div>
    <div class="tag">CORALVIEW OUTPATIENT SURGERY CENTER</div>
    <div class="tiny" style="position:absolute;right:5px;top:4px;text-align:right">42 Heron Gate Lane<br>Paget RH19 Bermuda<br>PO Box KM37<br>Devonshire LQTZ<br>info@ktlm-example.bm</div>
    <div class="tiny" style="margin-top:8px">Date</div>
    <div class="tiny" style="margin-top:1px"><b>Recipient Name</b><br>Company Name<br>Street Address<br>City, State, Zip</div>
    <div class="tiny" style="margin-top:3px">Dear patient, thank you for choosing our center for your outpatient care. Our team will guide you through every step before and after your visit.<br><br>Please bring your referral and insurance details on the day. Arrive early to complete your forms and speak with the nursing staff about any questions.<br><br>We look forward to welcoming you to the center.</div>
    <div class="tiny" style="margin-top:3px">Sincerely,</div>
    <div class="script" style="font-size:6px;line-height:6px">Signature</div>
    <div class="tiny"><b style="color:var(--blue)">Marisol Quenby-Harcourt</b></div>
    <div class="tiny foot">www.ktlm-example.bm</div>
  </div>
  <div class="label" style="left:109px;top:118px;width:78px">Letterhead option_01</div>

  <div class="piece" style="left:193px;top:16px;width:78px;height:101px;padding:4px 5px">
    <div style="text-align:center"><div class="mark" style="font-size:5px">KTLM</div><div class="tag">CORALVIEW OUTPATIENT SURGERY CENTER</div></div>
    <div class="tiny" style="margin-top:8px">Date</div>
    <div class="tiny" style="margin-top:1px"><b>Recipient Name</b><br>Company Name<br>Street Address<br>City, State, Zip</div>
    <div class="tiny" style="margin-top:3px">Dear patient, thank you for choosing our center for your outpatient care. Our team will guide you through every step before and after your visit.<br><br>Please bring your referral and insurance details on the day. Arrive early to complete your forms and speak with the nursing staff about any questions.<br><br>We look forward to welcoming you to the center.</div>
    <div class="tiny" style="margin-top:3px">Sincerely,</div>
    <div class="script" style="font-size:6px;line-height:6px">Signature</div>
    <div class="tiny"><b style="color:var(--blue)">Marisol Quenby-Harcourt</b></div>
    <div class="tiny foot" style="font-size:1.9px">42 Heron Gate Lane, Paget RH19 · PO Box KM37, Devonshire LQTZ<br>info@ktlm-example.bm · www.ktlm-example.bm</div>
  </div>
  <div class="label" style="left:193px;top:118px;width:78px">Letterhead option_02</div>

  <!-- email signature -->
  <div class="piece" style="left:293px;top:42px;width:53px;height:25px">
    <div style="position:absolute;right:0;top:0;width:19px;height:25px;background:var(--green)"></div>
    <div style="padding:2px 3px">
      <div class="mark" style="font-size:5px">KTLM</div>
      <div class="tiny" style="font-size:1.9px;line-height:2.5px;margin-top:1px"><b style="color:var(--blue)">Marisol Quenby-Harcourt</b><br>Director<br>T 441-555-0148<br>info@ktlm-example.bm</div>
    </div>
  </div>
  <div class="label" style="left:293px;top:69px;width:53px">Email Signature</div>

  <!-- envelopes -->
  <div class="piece" style="left:276px;top:80px;width:85px;height:38px;padding:3px 4px">
    <div class="mark" style="font-size:5px">KTLM</div>
    <div class="tag">CORALVIEW OUTPATIENT SURGERY CENTER</div>
    <div class="tiny" style="margin-top:1px">42 Heron Gate Lane, Paget RH19 Bermuda<br>PO Box KM37, Devonshire LQTZ</div>
  </div>
  <div class="label" style="left:276px;top:119px;width:85px">Envelope_Front</div>
  <div class="piece" style="left:365px;top:40px;width:84px;height:78px;background:#f4f4f4">
    <div style="height:14px;background:var(--blue);display:flex;align-items:center;justify-content:center"><span class="tiny light">www.ktlm-example.bm</span></div>
    <div style="height:14px;margin-top:8px;background:var(--green);display:flex;align-items:center;justify-content:center"><span class="tiny" style="color:#fff">www.ktlm-example.bm</span></div>
    <div style="text-align:center;margin-top:16px" class="tiny">www.ktlm-example.bm</div>
  </div>
  <div class="label" style="left:365px;top:119px;width:84px">Envelope_Back</div>

  <!-- folder -->
  <div class="piece" style="left:467px;top:18px;width:128px;height:100px;background:var(--blue)">
    <div style="position:absolute;left:4px;top:0;width:3px;height:100px;background:var(--green)"></div>
    <div style="position:absolute;left:62px;top:0;width:60px;height:72px;background:#fff;display:flex;flex-direction:column;align-items:center;justify-content:center">
      <div class="mark" style="font-size:8px">KTLM</div>
      <div class="tag" style="margin-top:.5px">CORALVIEW OUTPATIENT SURGERY CENTER</div>
    </div>
    <div style="position:absolute;left:122px;top:0;width:3px;height:72px;background:var(--green)"></div>
    <div class="tiny light" style="position:absolute;left:10px;top:62px">42 Heron Gate Lane<br>Paget RH19 Bermuda<br>PO Box KM37, Devonshire LQTZ<br>T 441-555-0148<br>info@ktlm-example.bm</div>
    <div style="position:absolute;left:82px;top:80px;width:22px;height:13px;background:#fff;padding:2px;transform:rotate(-8deg)">
      <div class="mark" style="font-size:3px">KTLM</div>
      <div class="tiny" style="font-size:1.4px;line-height:1.8px">Marisol Quenby-Harcourt<br>Director</div>
    </div>
  </div>
  <div class="label" style="left:467px;top:119px;width:128px">Folder</div>

  <!-- fax sheets -->
  <div class="piece" style="left:595px;top:16px;width:78px;height:101px;padding:4px 5px">
    <div class="mark" style="font-size:5px">KTLM</div>
    <div class="tag">CORALVIEW OUTPATIENT SURGERY CENTER</div>
    <div class="tiny" style="position:absolute;right:5px;top:4px;text-align:right">42 Heron Gate Lane<br>Paget RH19 Bermuda<br>info@ktlm-example.bm</div>
    <div class="tiny" style="margin-top:10px;display:grid;grid-template-columns:1fr 1fr;gap:1.5px 4px">
      <span class="field">To:<i></i></span><span class="field">From:<i></i></span><span class="field">Fax:<i></i></span><span class="field">Pages:<i></i></span><span class="field">Phone:<i></i></span><span class="field">Date:<i></i></span><span class="field">Re:<i></i></span><span class="field">CC:<i></i></span>
    </div>
    <div class="tiny" style="margin-top:4px">☐ Urgent ☐ For Review ☐ Please Reply ☐ Recycle<br><br><b>Comments:</b></div>
    <div class="tiny foot">www.ktlm-example.bm</div>
  </div>
  <div class="label" style="left:595px;top:118px;width:78px">Fax option_01</div>

  <div class="piece" style="left:678px;top:16px;width:78px;height:101px;padding:4px 5px">
    <div style="text-align:center"><div class="mark" style="font-size:5px">KTLM</div><div class="tag">CORALVIEW OUTPATIENT SURGERY CENTER</div></div>
    <div class="tiny" style="margin-top:8px;display:grid;grid-template-columns:1fr 1fr;gap:1.5px 4px">
      <span class="field">To:<i></i></span><span class="field">From:<i></i></span><span class="field">Fax:<i></i></span><span class="field">Pages:<i></i></span><span class="field">Phone:<i></i></span><span class="field">Date:<i></i></span><span class="field">Re:<i></i></span><span class="field">CC:<i></i></span>
    </div>
    <div class="tiny" style="margin-top:4px">☐ Urgent ☐ For Review ☐ Please Reply ☐ Recycle<br><br><b>Comments:</b></div>
    <div class="tiny foot" style="font-size:1.9px">42 Heron Gate Lane, Paget RH19 · PO Box KM37, Devonshire LQTZ · info@ktlm-example.bm</div>
  </div>
  <div class="label" style="left:678px;top:118px;width:78px">Fax option_02</div>

  <!-- compliment slip & thank you -->
  <div class="piece" style="left:770px;top:27px;width:86px;height:37px;padding:3px 4px">
    <div class="mark" style="font-size:5px">KTLM</div>
    <div class="tag">CORALVIEW OUTPATIENT<br>SURGERY CENTER</div>
    <div class="tiny" style="position:absolute;right:4px;top:3px;text-align:right">42 Heron Gate Lane<br>Paget RH19 Bermuda<br>PO Box KM37<br>info@ktlm-example.bm</div>
    <div class="script" style="font-size:8px;margin:5px 0 0 18px">With Compliments</div>
  </div>
  <div class="label" style="left:770px;top:65px;width:86px">Compliment Slip</div>
  <div class="piece" style="left:764px;top:73px;width:48px;height:37px;padding:3px;text-align:center">
    <div class="mark" style="font-size:5px">KTLM</div>
    <div class="tag">CORALVIEW OUTPATIENT SURGERY CENTER</div>
    <div class="script" style="font-size:8px;margin-top:4px">Thank you</div>
  </div>
  <div class="label" style="left:764px;top:111px;width:48px">Thank You Card_Front</div>
  <div class="piece" style="left:819px;top:73px;width:48px;height:37px;background:var(--blue)">
    <div class="tiny light foot" style="font-size:1.9px;line-height:2.5px">42 Heron Gate Lane, Paget RH19<br>PO Box KM37, Devonshire LQTZ<br>www.ktlm-example.bm</div>
  </div>
  <div class="label" style="left:819px;top:111px;width:48px">Thank You Card_Back</div>

  <!-- CD & screens -->
  <div class="disc" style="left:871px;top:7px;width:58px;height:58px;background:var(--blue)">
    <div class="top"><div class="mark light" style="font-size:5px">KTLM</div><div class="tag light">CORALVIEW OUTPATIENT SURGERY CENTER</div></div>
    <div class="hole"></div>
    <div class="url tiny light">www.ktlm-example.bm</div>
  </div>
  <div class="label" style="left:871px;top:66px;width:58px">CD</div>
  <div class="piece" style="left:935px;top:12px;width:56px;height:48px;padding:3px">
    <div style="position:absolute;left:0;top:0;right:0;height:8px;background:var(--blue)"></div>
    <div style="margin-top:8px"><div class="mark" style="font-size:5px">KTLM</div><div class="tag">CORALVIEW OUTPATIENT SURGERY CENTER</div></div>
    <div class="tiny" style="position:absolute;bottom:2px;left:3px;font-size:1.9px;line-height:2.5px">42 Heron Gate Lane, Paget RH19<br>info@ktlm-example.bm</div>
  </div>
  <div class="label" style="left:935px;top:62px;width:56px">CD cover</div>
  <div class="piece" style="left:873px;top:74px;width:58px;height:40px;background:var(--blue);display:flex;flex-direction:column;align-items:center;justify-content:center;border:2px solid #111">
    <div class="mark light" style="font-size:7px">KTLM</div>
    <div class="tag light">CORALVIEW OUTPATIENT SURGERY CENTER</div>
  </div>
  <div class="label" style="left:873px;top:116px;width:58px">iPad</div>
  <div class="piece" style="left:940px;top:74px;width:20px;height:38px;background:var(--blue);display:flex;align-items:center;justify-content:center;border:1.5px solid #fff">
    <div style="transform:rotate(-90deg);text-align:center;white-space:nowrap"><div class="mark light" style="font-size:4px">KTLM</div><div class="tag light" style="font-size:1.3px">OUTPATIENT SURGERY</div></div>
  </div>
  <div class="piece" style="left:966px;top:74px;width:20px;height:38px;background:#111;display:flex;align-items:center;justify-content:center">
    <div style="transform:rotate(-90deg);text-align:center;white-space:nowrap"><div class="mark light" style="font-size:4px">KTLM</div><div class="tag light" style="font-size:1.3px">OUTPATIENT SURGERY</div></div>
  </div>
  <div class="label" style="left:940px;top:116px;width:46px">iPhone</div>

  <!-- folder inner & magnets -->
  <div class="piece" style="left:475px;top:140px;width:125px;height:70px">
    <div style="position:absolute;left:0;top:0;width:3px;height:70px;background:var(--green)"></div>
    <div style="position:absolute;right:0;top:0;width:3px;height:70px;background:var(--green)"></div>
    <div style="position:absolute;left:8px;bottom:0;width:52px;height:26px;background:var(--blue)"></div>
    <div style="position:absolute;right:8px;bottom:0;width:52px;height:26px;background:var(--blue)"></div>
  </div>
  <div class="label" style="left:475px;top:212px;width:125px">Folder Inner</div>

  <div class="disc" style="left:485px;top:222px;width:22px;height:22px;background:#fff;border:1.5px solid var(--green)"><span class="mark" style="font-size:3.5px">KTLM</span><span class="tiny" style="font-size:1.2px;line-height:1.6px">www.ktlm-example.bm</span></div>
  <div class="disc" style="left:511px;top:222px;width:22px;height:22px;background:var(--blue)"><span class="mark light" style="font-size:3.5px">KTLM</span><span class="tiny light" style="font-size:1.2px;line-height:1.6px">www.ktlm-example.bm</span></div>
  <div class="disc" style="left:537px;top:222px;width:22px;height:22px;background:var(--green)"><span class="mark light" style="font-size:3.5px">KTLM</span><span class="tiny" style="font-size:1.2px;line-height:1.6px;color:#fff">www.ktlm-example.bm</span></div>
  <div class="disc" style="left:563px;top:222px;width:22px;height:22px;background:#fff;border:1.5px solid var(--blue)"><span class="mark" style="font-size:3.5px">KTLM</span><span class="tiny" style="font-size:1.2px;line-height:1.6px">www.ktlm-example.bm</span></div>
  <div class="label" style="left:485px;top:246px;width:100px">Car Magnet</div>

  <!-- CD labels -->
  <div class="disc" style="left:682px;top:128px;width:58px;height:58px;background:var(--blue);border:1px solid var(--green)">
    <div class="top"><div class="mark light" style="font-size:5px">KTLM</div><div class="tag light">CORALVIEW OUTPATIENT SURGERY CENTER</div></div>
    <div class="hole"></div><div class="url tiny light">www.ktlm-example.bm</div>
  </div>
  <div class="disc" style="left:748px;top:128px;width:58px;height:58px;background:var(--green)">
    <div class="top"><div class="mark light" style="font-size:5px">KTLM</div><div class="tag light" style="color:#fff">CORALVIEW OUTPATIENT SURGERY CENTER</div></div>
    <div class="hole"></div><div class="url tiny" style="color:#fff">www.ktlm-example.bm</div>
  </div>
  <div class="disc" style="left:682px;top:190px;width:58px;height:58px;background:#fff;border:2px solid var(--blue)">
    <div class="top"><div class="mark" style="font-size:5px">KTLM</div><div class="tag">CORALVIEW OUTPATIENT SURGERY CENTER</div></div>
    <div class="hole"></div><div class="url tiny">www.ktlm-example.bm</div>
  </div>
  <div class="disc" style="left:748px;top:190px;width:58px;height:58px;background:var(--blue);border:2px solid #fff">
    <div class="top"><div class="mark light" style="font-size:5px">KTLM</div><div class="tag light">CORALVIEW OUTPATIENT SURGERY CENTER</div></div>
    <div class="hole"></div><div class="url tiny light">www.ktlm-example.bm</div>
  </div>
  <div class="label" style="left:682px;top:249px;width:124px">CD</div>

  <!-- CD covers & devices -->
  <div class="piece" style="left:820px;top:143px;width:57px;height:40px;background:var(--blue);padding:3px">
    <div class="mark light" style="font-size:4.5px">KTLM</div>
    <div class="tag light">CORALVIEW OUTPATIENT SURGERY CENTER</div>
    <div class="tiny light" style="position:absolute;bottom:3px;left:3px;font-size:1.9px;line-height:2.5px">42 Heron Gate Lane, Paget RH19 Bermuda<br>T 441-555-0148 · info@ktlm-example.bm</div>
  </div>
  <div class="label" style="left:820px;top:184px;width:57px">CD cover</div>
  <div class="piece" style="left:820px;top:195px;width:57px;height:40px;padding:3px">
    <div class="mark" style="font-size:4.5px">KTLM</div>
    <div class="tag">CORALVIEW OUTPATIENT SURGERY CENTER</div>
    <div class="tiny" style="position:absolute;bottom:3px;left:3px;font-size:1.9px;line-height:2.5px">42 Heron Gate Lane, Paget RH19 Bermuda<br>T 441-555-0148 · info@ktlm-example.bm</div>
  </div>
  <div class="label" style="left:820px;top:236px;width:57px">CD cover</div>
  <div class="piece" style="left:892px;top:143px;width:55px;height:40px;display:flex;flex-direction:column;align-items:center;justify-content:center;border:3px solid #111">
    <span class="mark" style="font-size:6px">KTLM</span><span class="tag">CORALVIEW OUTPATIENT SURGERY CENTER</span>
  </div>
  <div class="label" style="left:892px;top:184px;width:55px">iPad</div>
  <div class="piece" style="left:892px;top:195px;width:55px;height:40px;background:#000;display:flex;flex-direction:column;align-items:center;justify-content:center">
    <span class="mark" style="font-size:6px">KTLM</span><span class="tag" style="color:var(--green)">CORALVIEW OUTPATIENT SURGERY CENTER</span>
  </div>
  <div class="label" style="left:892px;top:236px;width:55px">iPad</div>
  <div class="piece" style="left:962px;top:143px;width:19px;height:40px;display:flex;align-items:center;justify-content:center;border:1px solid #bbb">
    <div style="transform:rotate(-90deg);text-align:center;white-space:nowrap"><div class="mark" style="font-size:3.5px">KTLM</div><div class="tag" style="font-size:1.2px">OUTPATIENT SURGERY</div></div>
  </div>
  <div class="label" style="left:956px;top:184px;width:31px">iPhone</div>
  <div class="piece" style="left:962px;top:195px;width:19px;height:40px;background:#000;display:flex;align-items:center;justify-content:center">
    <div style="transform:rotate(-90deg);text-align:center;white-space:nowrap"><div class="mark" style="font-size:3.5px">KTLM</div><div class="tag" style="font-size:1.2px;color:var(--green)">OUTPATIENT SURGERY</div></div>
  </div>
  <div class="label" style="left:956px;top:236px;width:31px">iPhone</div>

  <!-- presentation slides -->
  <div class="piece" style="left:1001px;top:14px;width:96px;height:68px;text-align:center;padding-top:10px">
    <div class="mark" style="font-size:12px">KTLM</div>
    <div class="tag" style="font-size:2px">CORALVIEW OUTPATIENT SURGERY CENTER</div>
    <div style="font-size:4.2px;color:var(--blue);font-weight:600;margin-top:7px;line-height:5px">Welcome to Our<br>Presentation Name</div>
    <div style="font-size:3px;color:var(--green)">Description</div>
  </div>

  <div class="piece" style="left:1101px;top:14px;width:96px;height:68px;padding:4px 5px">
    <div class="slide-h">Heading Here</div><div class="slide-s">Sub Heading</div><div class="rule"></div>
    <div style="display:grid;grid-template-columns:repeat(4,1fr);gap:3px">
      <div class="photo" role="img" aria-label="Team member portrait" style="height:17px">Photo</div>
      <div class="photo" role="img" aria-label="Team member portrait" style="height:17px">Photo</div>
      <div class="photo" role="img" aria-label="Team member portrait" style="height:17px">Photo</div>
      <div class="photo" role="img" aria-label="Team member portrait" style="height:17px">Photo</div>
      <div class="tiny" style="font-size:2px;line-height:2.6px"><b style="color:var(--blue)">Team member1</b><br>Title<br>Short role note here</div>
      <div class="tiny" style="font-size:2px;line-height:2.6px"><b style="color:var(--blue)">Team member2</b><br>Title<br>Short role note here</div>
      <div class="tiny" style="font-size:2px;line-height:2.6px"><b style="color:var(--blue)">Team member3</b><br>Title<br>Short role note here</div>
      <div class="tiny" style="font-size:2px;line-height:2.6px"><b style="color:var(--blue)">Team member4</b><br>Title<br>Short role note here</div>
    </div>
  </div>

  <div class="piece" style="left:1001px;top:90px;width:96px;height:68px;padding:4px 5px">
    <div class="slide-h">Heading Here</div><div class="slide-s">Sub Heading</div><div class="rule"></div>
    <div style="display:grid;grid-template-columns:1fr 1fr;gap:2px 4px">
      <div class="tiny" style="font-size:2px;line-height:2.6px"><b style="color:var(--blue)">Group1</b><br>Brief summary of care steps and patient support.</div>
      <div class="tiny" style="font-size:2px;line-height:2.6px"><b style="color:var(--blue)">Group4</b><br>Brief summary of care steps and patient support.</div>
      <div class="tiny" style="font-size:2px;line-height:2.6px"><b style="color:var(--blue)">Group2</b><br>Brief summary of care steps and patient support.</div>
      <div class="tiny" style="font-size:2px;line-height:2.6px"><b style="color:var(--blue)">Group5</b><br>Brief summary of care steps and patient support.</div>
      <div class="tiny" style="font-size:2px;line-height:2.6px"><b style="color:var(--blue)">Group3</b><br>Brief summary of care steps and patient support.</div>
      <div class="tiny" style="font-size:2px;line-height:2.6px"><b style="color:var(--blue)">Group6</b><br>Brief summary of care steps and patient support.</div>
    </div>
  </div>

  <div class="piece" style="left:1101px;top:90px;width:96px;height:68px;padding:4px 5px">
    <div class="slide-h">Heading Here</div><div class="slide-s">Sub Heading</div><div class="rule"></div>
    <svg width="42" height="30" viewBox="0 0 42 30" style="position:absolute;left:8px;top:17px">
      <line x1="0" y1="29" x2="42" y2="29" stroke="#bbb" stroke-width=".4"/>
      <rect x="3" y="3" width="5" height="26" fill="var(--blue)"/>
      <rect x="11" y="8" width="5" height="21" fill="var(--blue)"/>
      <rect x="19" y="12" width="5" height="17" fill="var(--blue)"/>
      <rect x="27" y="17" width="5" height="12" fill="var(--blue)"/>
      <rect x="35" y="20" width="5" height="9" fill="var(--blue)"/>
    </svg>
    <div class="tiny" style="position:absolute;left:56px;top:17px;width:35px;font-size:2px;line-height:2.6px">Visits rose each quarter as new services opened and wait times fell across the year.</div>
    <div class="tiny" style="position:absolute;left:5px;top:52px;width:86px;font-size:2px;line-height:2.6px">Summary of yearly outpatient procedures across all departments and clinics.</div>
  </div>

  <div class="piece" style="left:1001px;top:165px;width:96px;height:68px;padding:4px 5px">
    <div class="slide-h">Heading Here</div><div class="slide-s">Sub Heading</div><div class="rule"></div>
    <div class="tiny" style="width:46px;font-size:2px;line-height:2.6px">Patient feedback gathered over the year shows high satisfaction with staff, timing and follow-up care.<br><br>Most patients said they would recommend the center to family and friends.</div>
    <svg width="22" height="22" viewBox="0 0 22 22" style="position:absolute;left:63px;top:18px">
      <circle cx="11" cy="11" r="10" fill="var(--blue)"/>
      <path d="M11 11 L11 1 A10 10 0 0 1 20.5 14 Z" fill="var(--green)"/>
    </svg>
    <div class="tiny" style="position:absolute;left:60px;top:43px;font-size:2px;line-height:2.6px"><span style="color:var(--blue)">■</span> Satisfied<br><span style="color:var(--green)">■</span> Neutral</div>
  </div>

  <div class="piece" style="left:1101px;top:165px;width:96px;height:68px;background:var(--blue);color:#fff;text-align:center;padding-top:18px">
    <div style="font-size:13px;font-weight:400;line-height:13px">Thanks</div>
    <div style="font-size:7px;font-weight:400">For Coming</div>
    <div class="tiny light foot" style="font-size:1.9px;line-height:2.5px">42 Heron Gate Lane, Paget RH19 · PO Box KM37, Devonshire LQTZ<br>T 441-555-0148 · info@ktlm-example.bm · www.ktlm-example.bm</div>
  </div>

</div>
</body>
</html>
```